Oversized Post Card for Busines Owners 1st 2nd and 3rd prizes

Create a professional, fresh and polished oversized post card for law firm specializing in Business Law, Succession Planning, and Employment Law

Use any picture(s) of your choice (mine or ones you recommend), logo, headshot and company info

www.morvenquaylegal.example

Westbrook Office - 4175 Hollister Avenue, Suite 1400, Charlotte, NC 28299
Kestrelmoor Office - 13840 Tamsin Way, Suite 300, Charlotte, NC 28296

Phone (704) 555-0187

Use this card for a Free Consultation

Target Market(s)

Business Owners (of small businesses)

Industry/Entity Type

Business

Font styles to use
Serif
Sans Serif

Requirements
Must have
• Company name, logo and contact info
• Serving business owners with legal guidance
• Business Law, Succession Planning & Wealth Transfers
• www.morvenquaylegal.example
• Westbrook Office - 4175 Hollister Avenue, Suite 1400, Charlotte, NC 28299
• Kestrelmoor Office - 13840 Tamsin Way, Suite 300, Charlotte, NC 28296
• Phone (704) 555-0187
• Use this card for a Free Consultation
Nice to have
• pictures (yours or mine) - you choose; headshot picture

```html
<!DOCTYPE html>
<html lang="en">
<head>
<meta charset="utf-8">
<title>Morven Quay Law, PLLC – Postcard</title>
<link href="https://fonts.googleapis.com/css2?family=Cinzel:wght@400;500;600;700&display=swap" rel="stylesheet">
<style>
  :root {
    --teal-light: #46e0c4;
    --teal: #2aa8a4;
    --teal-deep: #1e6f86;
    --ink: #1f1f1f;
    --ink-soft: #333333;
    --black: #111111;
    --white: #ffffff;
    --paper: #f7f9fb;
  }
  * { box-sizing: border-box; margin: 0; padding: 0; }
  html, body { width: 1200px; height: 776px; overflow: hidden; background: var(--white); }
  .postcard {
    position: relative; width: 1200px; height: 776px; overflow: hidden;
    background: linear-gradient(180deg, var(--white) 0%, var(--paper) 100%);
    font-family: "Cinzel", serif; color: var(--ink);
  }
  .photo-strip {
    position: absolute; left: 14px; top: 14px; width: 1173px; height: 204px;
    background: linear-gradient(180deg, var(--teal-light) 0%, var(--teal) 45%, var(--teal-deep) 100%);
  }
  .photo { position: absolute; top: 8px; height: 182px; }
  .photo--skyline { left: 12px; width: 278px; background: linear-gradient(180deg, #2b4f9a 0%, #1a2b55 55%, #3a2a1c 100%); }
  .photo--bulbs { left: 299px; width: 276px; background: radial-gradient(circle at 30% 50%, #5d7fa8 0%, #1c3d6b 45%, #0b1a33 100%); }
  .photo--chalkboard { left: 594px; width: 278px; background: radial-gradient(circle at 50% 45%, #3a3a3a 0%, #141414 100%); }
  .photo--estate { left: 882px; width: 280px; background: linear-gradient(120deg, #f3e6cc 0%, #e1c48f 55%, #a77a3a 100%); }

  .seal {
    position: absolute; left: 515px; top: 168px; width: 160px; height: 160px;
    border-radius: 50%; background: var(--white);
    border: 4px solid #222; box-shadow: 0 0 0 3px #cfd6da inset;
    display: flex; align-items: center; justify-content: center;
  }
  .seal__name {
    font-family: "Cinzel", serif; font-weight: 600; font-size: 19px;
    color: var(--teal-deep); text-align: center; line-height: 1.15;
  }

  .headshot-frame {
    position: absolute; left: 19px; top: 226px; width: 295px; height: 325px;
    background: linear-gradient(180deg, var(--teal-light) 0%, var(--teal-deep) 100%);
  }
  .headshot {
    position: absolute; left: 7px; top: 7px; width: 281px; height: 311px;
    background: radial-gradient(ellipse at 50% 40%, #d9b98a 0%, #8a6a48 35%, #2a2420 70%, #151515 100%);
  }

  .family-photo {
    position: absolute; left: 816px; top: 328px; width: 384px; height: 314px;
    background: radial-gradient(ellipse at 55% 55%, #f2e3d4 0%, #dfeef3 50%, rgba(255,255,255,0) 80%);
  }

  .firm { position: absolute; left: 340px; width: 520px; text-align: center; }
  .firm__rule { position: absolute; top: 339px; left: 364px; width: 470px; height: 2px; background: var(--black); }
  .firm__name {
    top: 346px; font-size: 54px; font-weight: 500; letter-spacing: 1px; line-height: 1;
    background: linear-gradient(180deg, var(--teal) 0%, var(--teal-deep) 100%);
    -webkit-background-clip: text; background-clip: text; color: transparent;
  }
  .firm__entity {
    top: 404px; font-size: 24px; color: var(--ink-soft);
    display: flex; align-items: center; justify-content: center; gap: 14px;
  }
  .firm__entity::before, .firm__entity::after { content: ""; width: 155px; height: 2px; background: var(--black); }
  .firm__services { top: 443px; left: 330px; width: 540px; font-size: 24.5px; line-height: 25px; color: var(--ink-soft); letter-spacing: .5px; }
  .firm__phone { top: 496px; font-size: 44px; font-weight: 500; color: var(--ink-soft); line-height: 1; }

  .offer {
    position: absolute; left: 364px; top: 548px; width: 446px; height: 58px;
    background: var(--black); color: var(--white); text-align: center;
  }
  .offer__lead { display: block; font-size: 15px; letter-spacing: 5px; line-height: 18px; padding-top: 2px; }
  .offer__main { display: block; font-size: 38px; line-height: 36px; letter-spacing: .5px; }
  .firm__url { top: 611px; font-size: 22px; font-weight: 600; color: var(--ink-soft); }

  .footer {
    position: absolute; left: 0; top: 642px; width: 1200px; height: 104px;
    background: var(--black); color: var(--white); text-align: center;
  }
  .footer__office { font-size: 19px; line-height: 23px; letter-spacing: .2px; }
  .footer__office:first-child { padding-top: 6px; }
  .footer__office strong { font-weight: 500; }
  .social { display: flex; justify-content: center; gap: 10px; margin-top: 8px; }
  .social__link {
    width: 42px; height: 42px;
    background: linear-gradient(180deg, var(--teal-light) 0%, var(--teal-deep) 100%);
  }
  .tagline {
    position: absolute; left: 0; top: 746px; width: 1200px; height: 30px;
    background: linear-gradient(180deg, var(--teal-light) 0%, var(--teal) 100%);
    color: var(--white); text-align: center; font-size: 15px; letter-spacing: 6.5px; line-height: 30px;
  }
</style>
</head>
<body>
<main class="postcard">
  <section class="photo-strip">
    <div class="photo photo--skyline" role="img" aria-label="Charlotte city skyline at dusk"></div>
    <div class="photo photo--bulbs" role="img" aria-label="Row of light bulbs with one glowing"></div>
    <div class="photo photo--chalkboard" role="img" aria-label="Chalkboard listing estate planning topics"></div>
    <div class="photo photo--estate" role="img" aria-label="Estate documents with house keys and coins"></div>
  </section>

  <div class="seal"><span class="seal__name">Morven<br>Quay</span></div>

  <div class="headshot-frame">
    <div class="headshot" role="img" aria-label="Portrait of the attorney"></div>
  </div>

  <div class="family-photo" role="img" aria-label="Smiling family of four looking upward"></div>

  <div class="firm__rule"></div>
  <h1 class="firm firm__name">MORVEN QUAY</h1>
  <p class="firm firm__entity">LAW, PLLC</p>
  <p class="firm firm__services">BUSINESS LAW, SUCCESSION PLANNING<br>&amp; WEALTH TRANSFERS</p>
  <p class="firm firm__phone">PHONE (704) 555-0187</p>

  <div class="offer">
    <span class="offer__lead">USE THIS CARD FOR A</span>
    <span class="offer__main">FREE CONSULTATION</span>
  </div>
  <p class="firm firm__url">WWW.MORVENQUAYLEGAL.EXAMPLE</p>

  <footer class="footer">
    <p class="footer__office"><strong>WESTBROOK OFFICE</strong> - 4175 HOLLISTER AVENUE, SUITE 1400, CHARLOTTE, NC 28299</p>
    <p class="footer__office"><strong>KESTRELMOOR OFFICE</strong> - 13840 TAMSIN WAY, SUITE 300, CHARLOTTE, NC 28296</p>
    <div class="social">
      <span class="social__link" role="img" aria-label="Social profile"></span>
      <span class="social__link" role="img" aria-label="Social profile"></span>
      <span class="social__link" role="img" aria-label="Social profile"></span>
    </div>
  </footer>
  <p class="tagline">SERVING BUSINESS OWNERS WITH LEGAL GUIDANCE</p>
</main>
</body>
</html>
```